Quenby Bespoke Furnishings logo and business card

Quenby is a female operated furniture design and reupholstery business. Working with luxury top end fabrics and furnishings for unique and stylish one off designs. Bringing loved pieces of furniture back to life by recovering on modern, trendy, stylish fabrics. Think Velvet chaise lounge or velour Chesterfield lounges, vibrant and unique colourful, individually designed statement pieces.
We would like a simple logo that can be used on socials and a business card that is simple yet striking . Possibly using a bronze or gold foil.
The business name is QUENBY BESPOKE FURNISHINGS
Can be just QUENBY
Logo will be used on socials and images of finished furniture.

Target Market(s)

high end luxury holiday houses. Artistic flair designer houses

Industry/Entity Type

Home Furniture

Contact Information for Business Card

Simple yet designer
Logo on the front and name details on the back

Font styles to use
Decorative

Requirements
Must have
• Finess
A feel of artistic design
Just a logo/business name on the front of the card
Should not have
• not a picture of furniture

```html
<!DOCTYPE html>
<html lang="en">
<head>
<meta charset="utf-8">
<title>Quenby Bespoke Furnishings – Business Card</title>
<link rel="stylesheet" href="https://fonts.googleapis.com/css2?family=Cinzel:wght@500&family=Montserrat:wght@400;600;700&display=swap">
<style>
  :root {
    --backdrop: #1f1f1f;
    --amber-light: #ecb11f;
    --amber-mid: #e98b0c;
    --amber-deep: #e05f00;
    --paper: #ffffff;
    --ink: #2a2a2a;
    --arc: #333333;
  }
  * { box-sizing: border-box; margin: 0; padding: 0; }
  html, body { width: 1200px; height: 1015px; overflow: hidden; }
  body {
    background: var(--backdrop);
    font-family: "Montserrat", Arial, sans-serif;
    display: flex;
    flex-direction: column;
    align-items: center;
    justify-content: center;
    gap: 56px;
  }
  .card {
    position: relative;
    width: 760px;
    height: 434px;
    overflow: hidden;
    background: linear-gradient(160deg, var(--amber-light) 0%, var(--amber-mid) 45%, var(--amber-deep) 100%);
    box-shadow: 0 14px 30px rgba(0,0,0,0.55);
  }
  .wordmark {
    position: absolute;
    display: flex;
    flex-direction: column;
    align-items: center;
    text-align: center;
  }
  .wordmark-name {
    font-family: "Cinzel", "Times New Roman", serif;
    font-weight: 500;
    line-height: 1;
  }
  .wordmark-tagline {
    font-family: "Montserrat", Arial, sans-serif;
    font-weight: 700;
    text-transform: uppercase;
  }
  /* Front */
  .card-front .wordmark {
    left: 0; right: 0; top: 150px;
    color: var(--paper);
  }
  .card-front .wordmark-name { font-size: 104px; letter-spacing: 6px; }
  .card-front .wordmark-tagline { font-size: 15px; letter-spacing: 7px; margin-top: 14px; }
  /* Back */
  .card-back-shape { position: absolute; inset: 0; }
  .card-back .wordmark {
    left: 430px; width: 310px; top: 150px;
    color: var(--ink);
  }
  .card-back .wordmark-name { font-size: 62px; letter-spacing: 4px; }
  .card-back .wordmark-tagline { font-size: 9.5px; letter-spacing: 4px; margin-top: 10px; }
  .holder {
    position: absolute;
    left: 64px; top: 112px;
    color: var(--paper);
  }
  .holder-name { font-weight: 700; font-size: 25px; letter-spacing: 0.5px; }
  .holder-role { font-weight: 400; font-size: 19px; margin-top: 2px; }
  .address {
    position: absolute;
    left: 100px; top: 236px;
    color: var(--paper);
    font-size: 16px;
    line-height: 1.35;
  }
  .contact-list {
    position: absolute;
    left: 100px; top: 316px;
    list-style: none;
    color: var(--paper);
    font-size: 16px;
    line-height: 1.5;
  }
  .contact-list li { display: flex; align-items: center; gap: 10px; }
  .contact-icon { width: 18px; height: 18px; flex: none; }
</style>
</head>
<body>

  <section class="card card-front" aria-label="Card front">
    <div class="wordmark">
      <span class="wordmark-name">QUENBY</span>
      <span class="wordmark-tagline">Bespoke Furnishings</span>
    </div>
  </section>

  <section class="card card-back" aria-label="Card back">
    <svg class="card-back-shape" width="760" height="434" viewBox="0 0 760 434" aria-hidden="true">
      <circle cx="660" cy="150" r="300" fill="var(--paper)"/>
      <rect x="700" y="0" width="60" height="434" fill="var(--paper)"/>
      <path d="M389 70 A283 283 0 0 0 619 430" fill="none" stroke="var(--arc)" stroke-width="4" stroke-linecap="round"/>
    </svg>

    <div class="holder">
      <p class="holder-name">MARCUS HALE</p>
      <p class="holder-role">Managing Director</p>
    </div>

    <p class="address">17, Linden Row<br>Harbour Vale, 45821</p>

    <ul class="contact-list">
      <li>
        <svg class="contact-icon" viewBox="0 0 24 24" aria-hidden="true"><path fill="#fff" d="M6.6 10.8a15.5 15.5 0 0 0 6.6 6.6l2.2-2.2c.3-.3.7-.4 1-.2 1.1.4 2.3.6 3.6.6.6 0 1 .4 1 1V20c0 .6-.4 1-1 1A17 17 0 0 1 3 4c0-.6.4-1 1-1h3.5c.6 0 1 .4 1 1 0 1.3.2 2.5.6 3.6.1.3 0 .7-.2 1z"/></svg>
        044-987 650 312
      </li>
      <li>
        <svg class="contact-icon" viewBox="0 0 24 24" aria-hidden="true"><path fill="#fff" d="M2 5h20v14H2z"/><path fill="none" stroke="#e98b0c" stroke-width="1.8" d="M2 5l10 8 10-8"/></svg>
        hello@quenbyfurnishings.com
      </li>
      <li>
        <svg class="contact-icon" viewBox="0 0 24 24" aria-hidden="true"><g fill="none" stroke="#fff" stroke-width="1.8"><circle cx="12" cy="12" r="9.5"/><ellipse cx="12" cy="12" rx="4.2" ry="9.5"/><path d="M2.5 12h19M4 7h16M4 17h16"/></g></svg>
        www.quenbyfurnishings.com
      </li>
    </ul>

    <div class="wordmark">
      <span class="wordmark-name">QUENBY</span>
      <span class="wordmark-tagline">Bespoke Furnishings</span>
    </div>
  </section>

</body>
</html>
```